Business Card Design

Consultation for design, construction athletic facilities specializing in synthetic turf systems and all weather running track systems.
Motto "True Owner Representation"
New Company that we'd like to highlight the LOGO first and foremost with the colors of the background and font as primary colors of the card too if possible. I've also attached a typical larger project design layout that could be used in the background to highlight our design and construction specialty.
Website is something we want very noticeable for driving traffic.
Target Market(s)
Athletic Directors, Designers, Government and Military, Contractors
Industry/Entity Type
Construction
Contact Information for Business Card
Peter L. Vandrell CFB, CTB
48317 W 63rd Ave
Harlow Ridge, WA 99482
C +1 503.555.0147
O +1 808.555.0182
Peter@fieldlaneco.example
www.fieldlaneco.example

```html
<!DOCTYPE html>
<html lang="en">
<head>
<meta charset="utf-8">
<title>Nolvane Sport – Business Card</title>
<link rel="stylesheet" href="https://fonts.googleapis.com/css2?family=Cinzel:wght@400;600&display=swap">
<style>
  :root {
    --backdrop: #3a2c1e;
    --card-black: #0b0b0c;
    --card-edge: #1c1c1e;
    --gold: #e8b62a;
    --gold-pale: #e9cfa0;
    --glow-core: #fff6d8;
    --glow-mid: #f2c431;
    --glow-deep: #7a5a0e;
    --text-light: #e6e3dc;
  }
  * { box-sizing: border-box; margin: 0; padding: 0; }
  html, body { width: 1200px; height: 795px; overflow: hidden; }
  body {
    background: var(--backdrop);
    font-family: "Cinzel", "Times New Roman", serif;
    position: relative;
  }
  .business-card {
    position: absolute;
    top: 249px;
    width: 520px;
    height: 297px;
    background: radial-gradient(ellipse at 60% 30%, #1d1d20 0%, var(--card-black) 70%);
    border: 1px solid var(--card-edge);
    box-shadow: 0 14px 30px rgba(0,0,0,.55);
    overflow: hidden;
  }
  .card-front { left: 60px; }
  .card-back { left: 620px; }

  .eclipse-artwork {
    position: absolute;
    left: -40px;
    bottom: -60px;
    width: 330px;
    height: 300px;
    background:
      radial-gradient(circle at 48% 66%, var(--glow-core) 0%, rgba(255,230,150,.9) 10%, rgba(242,196,49,.55) 26%, rgba(122,90,14,.25) 48%, rgba(0,0,0,0) 68%);
  }

  .contact-block {
    position: absolute;
    right: 30px;
    top: 34px;
    text-align: right;
  }
  .holder-name {
    color: var(--gold);
    font-weight: 600;
    font-size: 21px;
    letter-spacing: .5px;
    line-height: 1.2;
  }
  .holder-credentials {
    color: var(--gold);
    font-weight: 600;
    font-size: 19px;
    margin-bottom: 16px;
  }
  .contact-line {
    color: var(--text-light);
    font-size: 11.5px;
    letter-spacing: .6px;
    line-height: 1.75;
  }
  .line-tag {
    color: var(--gold);
    margin-left: 4px;
  }
  .street-address {
    position: absolute;
    right: 30px;
    bottom: 22px;
    color: var(--text-light);
    font-size: 11.5px;
    letter-spacing: .6px;
  }

  .brand-mark {
    position: absolute;
    left: 50%;
    top: 50%;
    transform: translate(-50%, -50%);
    display: flex;
    align-items: center;
    gap: 14px;
  }
  .brand-dot {
    width: 14px;
    height: 14px;
    border-radius: 50%;
    background: var(--gold-pale);
  }
  .brand-name {
    color: var(--gold-pale);
    font-weight: 400;
    font-size: 30px;
    letter-spacing: 5px;
  }
</style>
</head>
<body>
  <section class="business-card card-front">
    <div class="eclipse-artwork" role="img" aria-label="Golden eclipse burst artwork"></div>
    <div class="contact-block">
      <p class="holder-name">Peter L. Vandrell</p>
      <p class="holder-credentials">CFB, CTB</p>
      <p class="contact-line">+1 503.555.0147<span class="line-tag">C</span></p>
      <p class="contact-line">+1 808.555.0182<span class="line-tag">P</span></p>
      <p class="contact-line">Peter@fieldlaneco.example</p>
      <p class="contact-line">www.fieldlaneco.example</p>
    </div>
    <p class="street-address">48317 W 63rd Ave Harlow Ridge, WA 99482</p>
  </section>

  <section class="business-card card-back">
    <div class="brand-mark">
      <span class="brand-dot"></span>
      <span class="brand-name">Nolvane Sport</span>
    </div>
  </section>
</body>
</html>
```